Trade Show Marlow 3x3 booth schel scheme

We would like to have full coverage design for 3x3 booth scheel

2x2 pop up Counter (1200mm wide x 900mm high x 400mm deep)
Our company provides food safety training, consultancy and food safety app service for hospitality businesses.

```html
<!DOCTYPE html>
<html lang="en">
<head>
<meta charset="utf-8">
<title>Kestrow – Trade Show Booth Scheme</title>
<link rel="stylesheet" href="https://fonts.googleapis.com/css2?family=Anton&family=Montserrat:wght@500;700&family=Archivo:wght@700&display=swap">
<style>
  :root {
    --lime: #c5cf2a;
    --lime-soft: #d3db4a;
    --ink: #000000;
    --paper: #f5f5f5;
    --white: #ffffff;
    --stage: #8a8a8a;
    --counter: #dcdcdc;
    --display: "Anton", "Impact", sans-serif;
    --brand: "Montserrat", "Helvetica", sans-serif;
    --band: "Archivo", "Arial", sans-serif;
  }
  * { box-sizing: border-box; margin: 0; padding: 0; }
  html, body { width: 1200px; height: 733px; overflow: hidden; background: var(--stage); }
  .booth { position: relative; width: 1200px; height: 733px; }

  .panel { position: absolute; background: var(--paper); overflow: hidden; }

  /* brand lockup */
  .brand { display: flex; align-items: center; gap: 8px; font-family: var(--brand); font-weight: 500; letter-spacing: .22em; color: var(--ink); }
  .brand-dot { border-radius: 50%; background: var(--lime); flex: none; }
  .tagline { font-family: var(--brand); font-weight: 500; letter-spacing: .12em; text-transform: uppercase; line-height: 1.25; }
  .lockup { display: flex; align-items: center; gap: 6px; }
  .lockup .rule { width: 1px; align-self: stretch; }

  .decor { position: absolute; background: radial-gradient(circle at 40% 40%, var(--lime-soft), var(--lime)); border-radius: 48% 52% 46% 54%; }

  /* service icons */
  .service { display: flex; flex-direction: column; align-items: center; text-align: center; }
  .service-icon { border-radius: 50%; background: var(--white); border: 3px solid var(--lime); display: flex; align-items: center; justify-content: center; }
  .service-icon svg { width: 55%; height: 55%; }
  .service-kind { color: var(--white); text-transform: uppercase; }
  .service-name { color: var(--lime); text-transform: uppercase; }

  /* left roll-up */
  .rollup-left { left: 30px; top: 90px; width: 190px; height: 560px; }
  .rollup-left .brand-band { position: absolute; top: 50px; left: 0; right: 0; height: 46px; background: var(--ink); display: flex; align-items: center; justify-content: center; }
  .rollup-left .brand { color: var(--white); font-size: 13px; gap: 5px; }
  .rollup-left .tagline { color: var(--white); font-size: 5px; }
  .rollup-left .rule { background: var(--white); }
  .rollup-left .headline { position: absolute; top: 112px; left: 0; right: 0; text-align: center; font-family: var(--display); font-weight: 400; text-transform: uppercase; line-height: 1.08; }
  .rollup-left .headline span { display: block; }
  .rollup-left .h-food { font-size: 22px; color: var(--ink); }
  .rollup-left .h-hygiene { font-size: 32px; color: var(--lime); }
  .rollup-left .h-health { font-size: 40px; color: var(--ink); }
  .rollup-left .h-safety { font-size: 32px; color: var(--lime); }
  .rollup-left .edge { position: absolute; right: 0; bottom: 0; width: 28px; height: 220px; background: var(--ink); border-top-left-radius: 100% 40%; }
  .rollup-left .decor { left: 14px; bottom: 24px; width: 150px; height: 210px; }

  /* back wall */
  .backwall { left: 245px; top: 90px; width: 710px; height: 420px; }
  .backwall .brand-top { position: absolute; top: 40px; left: 0; right: 0; display: flex; justify-content: center; }
  .backwall .brand { font-size: 54px; letter-spacing: .28em; gap: 14px; }
  .backwall .brand-dot { width: 26px; height: 26px; }
  .backwall .headline { position: absolute; left: 44px; top: 150px; font-family: var(--display); font-weight: 400; text-transform: uppercase; line-height: 1.05; }
  .backwall .h-line1 { font-size: 38px; color: var(--ink); display: block; }
  .backwall .h-line2 { font-size: 56px; color: var(--lime); display: block; }
  .backwall .provides { position: absolute; left: 44px; top: 268px; font-family: var(--brand); font-weight: 700; font-size: 20px; text-transform: uppercase; color: var(--ink); }
  .backwall .sector { position: absolute; left: 0; top: 300px; width: 380px; height: 32px; background: var(--lime); color: var(--white); font-family: var(--band); font-size: 19px; text-transform: uppercase; display: flex; align-items: center; padding-left: 44px; }
  .backwall .services { position: absolute; left: 0; top: 332px; width: 410px; height: 88px; background: var(--ink); clip-path: polygon(0 0, 92% 0, 100% 100%, 0 100%); display: flex; gap: 22px; padding: 8px 0 0 30px; }
  .backwall .service-icon { width: 44px; height: 44px; }
  .backwall .service-kind { font-family: var(--band); font-size: 8px; margin-top: 4px; }
  .backwall .service-name { font-family: var(--band); font-size: 10px; }
  .backwall .decor { right: 20px; top: 140px; width: 300px; height: 270px; }
  .backwall .edge { position: absolute; right: 0; top: 200px; width: 22px; height: 220px; background: var(--ink); border-top-left-radius: 100% 30%; }

  /* right roll-up */
  .rollup-right { left: 980px; top: 90px; width: 190px; height: 560px; }
  .rollup-right .provides { position: absolute; top: 60px; left: 0; right: 0; text-align: center; font-family: var(--display); font-size: 20px; line-height: 1.15; text-transform: uppercase; color: var(--ink); }
  .rollup-right .sector { position: absolute; top: 128px; left: 0; right: 0; height: 96px; background: var(--lime); text-align: center; font-family: var(--display); text-transform: uppercase; color: var(--white); line-height: 1.1; padding-top: 10px; }
  .rollup-right .sector span { display: block; }
  .rollup-right .s-1 { font-size: 34px; }
  .rollup-right .s-2 { font-size: 26px; }
  .rollup-right .services { position: absolute; top: 224px; left: 0; right: 0; height: 240px; background: var(--ink); clip-path: polygon(0 0, 100% 0, 100% 100%, 0 80%); display: grid; grid-template-columns: 1fr 1fr; align-content: start; row-gap: 12px; padding: 16px 10px 0; }
  .rollup-right .service:last-child { grid-column: 1 / span 2; }
  .rollup-right .service-icon { width: 40px; height: 40px; }
  .rollup-right .service-kind { font-family: var(--display); font-size: 8px; margin-top: 5px; }
  .rollup-right .service-name { font-family: var(--display); font-size: 11px; }
  .rollup-right .decor { left: 66px; bottom: 8px; width: 120px; height: 118px; }

  /* counter wrap */
  .counter { left: 500px; top: 540px; width: 200px; height: 150px; background: var(--counter); display: flex; align-items: center; justify-content: center; }
  .counter .brand { font-size: 12px; gap: 5px; }
  .counter .tagline { font-size: 5px; color: var(--ink); }
  .counter .rule { background: var(--ink); }
</style>
</head>
<body>
<main class="booth">

  <!-- left roll-up banner -->
  <section class="panel rollup-left">
    <div class="brand-band">
      <div class="lockup">
        <span class="brand">KESTROW<span class="brand-dot" style="width:7px;height:7px"></span></span>
        <span class="rule"></span>
        <span class="tagline">Food hygiene<br>&amp; health safety</span>
      </div>
    </div>
    <h2 class="headline">
      <span class="h-food">Food</span>
      <span class="h-hygiene">Hygiene &amp;</span>
      <span class="h-health">Health</span>
      <span class="h-safety">Safety</span>
    </h2>
    <div class="edge"></div>
    <div class="decor" role="img" aria-label="Large green apple with tick decoration"></div>
  </section>

  <!-- curved back wall -->
  <section class="panel backwall">
    <div class="brand-top">
      <span class="brand">KESTROW<span class="brand-dot"></span></span>
    </div>
    <div class="decor" role="img" aria-label="Large green apple with tick decoration"></div>
    <div class="edge"></div>
    <h1 class="headline">
      <span class="h-line1">Food Hygiene &amp;</span>
      <span class="h-line2">Health Safety</span>
    </h1>
    <p class="provides">Our company provides</p>
    <p class="sector">Hospitality businesses</p>
    <div class="services">
      <div class="service">
        <span class="service-icon"><svg viewBox="0 0 24 24"><path d="M5 12l5 5 9-10" fill="none" stroke="#000" stroke-width="3" stroke-linecap="round" stroke-linejoin="round"/></svg></span>
        <span class="service-kind">Food safety</span>
        <span class="service-name">Training</span>
      </div>
      <div class="service">
        <span class="service-icon"><svg viewBox="0 0 24 24"><path d="M5 12l5 5 9-10" fill="none" stroke="#000" stroke-width="3" stroke-linecap="round" stroke-linejoin="round"/></svg></span>
        <span class="service-kind">Food safety</span>
        <span class="service-name">Consultancy</span>
      </div>
      <div class="service">
        <span class="service-icon"><svg viewBox="0 0 24 24"><path d="M5 12l5 5 9-10" fill="none" stroke="#000" stroke-width="3" stroke-linecap="round" stroke-linejoin="round"/></svg></span>
        <span class="service-kind">Food safety</span>
        <span class="service-name">App service</span>
      </div>
    </div>
  </section>

  <!-- right roll-up banner -->
  <section class="panel rollup-right">
    <p class="provides">Our company<br>provides</p>
    <p class="sector"><span class="s-1">Hospitality</span><span class="s-2">Businesses</span></p>
    <div class="services">
      <div class="service">
        <span class="service-icon"><svg viewBox="0 0 24 24"><path d="M5 12l5 5 9-10" fill="none" stroke="#000" stroke-width="3" stroke-linecap="round" stroke-linejoin="round"/></svg></span>
        <span class="service-kind">Food safety</span>
        <span class="service-name">Training</span>
      </div>
      <div class="service">
        <span class="service-icon"><svg viewBox="0 0 24 24"><path d="M5 12l5 5 9-10" fill="none" stroke="#000" stroke-width="3" stroke-linecap="round" stroke-linejoin="round"/></svg></span>
        <span class="service-kind">Food safety</span>
        <span class="service-name">Consultancy</span>
      </div>
      <div class="service">
        <span class="service-icon"><svg viewBox="0 0 24 24"><path d="M5 12l5 5 9-10" fill="none" stroke="#000" stroke-width="3" stroke-linecap="round" stroke-linejoin="round"/></svg></span>
        <span class="service-kind">Food safety</span>
        <span class="service-name">App service</span>
      </div>
    </div>
    <div class="decor" role="img" aria-label="Green apple with tick decoration"></div>
  </section>

  <!-- pop-up counter wrap -->
  <section class="panel counter">
    <div class="lockup">
      <span class="brand">KESTROW<span class="brand-dot" style="width:7px;height:7px"></span></span>
      <span class="rule"></span>
      <span class="tagline">Food hygiene<br>&amp; health safety</span>
    </div>
  </section>

</main>
</body>
</html>
```